Postcard for NYC Education Class

The Larchfield Adult Learning Hub, an adult education center in New York City, seeks a postcard design to promote a classroom course called the Campus Pathway Seminar. The course walks adult learners through the college admissions, financial aid, and college enrollment processes.

You can learn more about the LALH and the LALH Scholar Bridge Initiative at http://lalh.wtcc.pvnu.edu/ and http://lalhscholarbridge.org/.

The postcard should have text on two-sides.

SIDE #1
[LALH Logo]
Campus Pathway Seminar
A Classroom Course for LALH Students Interested in College-Going

Daytime Schedule: Wednesdays, 12:20 pm – 3:00 pm
Evening Schedule: Wednesdays, 5:00 pm – 6:15 pm

To learn more and enroll, visit the Scholar Bridge Initiative in Room 1412 on your registration day. Apply now to guarantee a space!

SIDE #2
College Bound [in big Times New Roman Font in orange against a navy background…see http://lalh.wtcc.pvnu.edu/?page_id=1279&album=1&gallery=9]

[Sponsor Line: A sponsor line should appear in small italicized type on the front or back.]
The Larchfield Adult Learning Hub is administered by Westbrook Township Community College/PVNU.

[Testimonial Quote: A testimonial quote should go on the front or on the back, preferably the back. ]
“Before taking the Campus Pathway Seminar, I wasn't sure how I would even start. The Workshop provided me with the information that I needed to go back to college.” -CPS Participant Spring 2013, Currently Attending Ravelin Community College

Nice designs!  I like the designs by Studio of Norma and Bright Quill themost.  

Target Market(s)

Adult education students, ages 18-40+.

The postcard will be distributed to prospective students in person. It will not be mailed and does not need to be designed for mailing.

Industry/Entity Type

Financial

Requirements
Must have
• The LALH is on its way towards having an official style guide. In the meantime, models that you can use are at http://lalhscholarbridge.files.blogvessel.com/2013/06/cat-test-prep-workshop-postcard-final.pdf and at http://lalhscholarbridge.files.blogvessel.com/2013/06/fee-waiver-1.pdf.

Also at https://pages.sitenook.com/site/forwardlearnerplans/home/campus-pathway-seminar/CPS%20Fall%202013%20Foamcore%20v1%20PDF.pdf?attredirects=0&d=1.

The colors are white, navy (pantone 533?), and yellow/orange.
Nice to have
• A scalloped border like in the postcard at http://lalhscholarbridge.files.blogvessel.com/2013/06/cat-test-prep-workshop-postcard-final.pdf would be nice but is not necessary.

```html
<!DOCTYPE html>
<html lang="en">
<head>
<meta charset="utf-8">
<title>Campus Pathway Seminar Postcard</title>
<link rel="stylesheet" href="https://fonts.googleapis.com/css2?family=Tinos:wght@700&family=PT+Sans:ital,wght@0,400;0,700;1,700&family=Handlee&display=swap">
<style>
  :root {
    --navy: #1c2d5a;
    --yellow: #f1d815;
    --white: #ffffff;
    --ink: #111111;
    --backdrop: #ececec;
    --photo-light: #e9ecf2;
    --photo-warm: #b98a6a;
  }
  * { margin: 0; padding: 0; box-sizing: border-box; }
  html, body { width: 1200px; height: 1200px; overflow: hidden; }
  body {
    background: radial-gradient(circle at 70% 30%, #fafafa, var(--backdrop));
    position: relative;
    font-family: "PT Sans", Arial, sans-serif;
  }
  .card {
    position: absolute;
    width: 750px;
    height: 576px;
    box-shadow: 0 2px 6px rgba(0,0,0,0.18);
  }

  /* ---------- Side 1 ---------- */
  .side-front {
    left: 38px; top: 14px;
    background: var(--navy);
    padding: 12px;
  }
  .side-front .inner {
    width: 100%; height: 100%;
    border: 5px solid var(--yellow);
    background: var(--white);
    position: relative;
    text-align: center;
    color: var(--navy);
  }
  .brand {
    display: flex; align-items: center; justify-content: center; gap: 8px;
    font-family: "PT Sans", Arial, sans-serif;
    font-weight: 700;
    font-size: 22px;
    color: var(--navy);
    letter-spacing: 0.5px;
  }
  .brand .mark { width: 26px; height: 26px; background: var(--navy); flex: none; }
  .side-front .brand { position: absolute; top: 28px; left: 0; right: 0; }
  .title {
    position: absolute; top: 96px; left: 0; right: 0;
    font-family: "Tinos", "Times New Roman", serif;
    font-weight: 700;
    font-size: 56px;
    line-height: 54px;
    letter-spacing: 0.5px;
    transform: scaleX(0.92);
  }
  .subtitle {
    position: absolute; top: 206px; left: 0; right: 0;
    font-weight: 700;
    font-size: 25px;
    line-height: 27px;
  }
  .feature {
    position: absolute; left: 73px; top: 278px;
    width: 578px; height: 190px;
    background: var(--navy);
    padding: 6px;
    display: flex;
  }
  .feature .photo {
    width: 360px; height: 178px;
    background: linear-gradient(160deg, var(--photo-light) 55%, var(--photo-warm));
  }
  .schedule {
    color: var(--white);
    text-align: left;
    padding: 18px 0 0 20px;
    font-size: 17px;
    line-height: 22px;
  }
  .schedule dt { font-weight: 700; font-size: 18px; }
  .schedule dd { padding-left: 20px; margin-bottom: 8px; }
  .enroll {
    position: absolute; top: 476px; left: 0; right: 0;
    color: var(--ink);
    font-size: 15.5px;
    line-height: 18px;
  }
  .enroll strong { font-weight: 700; }

  /* ---------- Side 2 ---------- */
  .side-back {
    left: 406px; top: 598px;
    background: var(--navy);
  }
  .side-back .frame {
    position: absolute; left: 38px; top: 38px; right: 22px; bottom: 30px;
    border: 3px solid var(--yellow);
  }
  .side-back .band {
    position: absolute; left: 48px; right: 30px; top: 311px; bottom: 38px;
    background: var(--white);
  }
  .headline {
    position: absolute; top: 70px; left: 0; right: 0;
    text-align: center;
    font-family: "Tinos", "Times New Roman", serif;
    font-weight: 700;
    font-size: 86px;
    color: var(--yellow);
    transform: scaleX(0.63);
  }
  .note {
    position: absolute; left: 119px; top: 230px;
    width: 508px; height: 216px;
    background: var(--yellow);
    border-radius: 6px;
    padding: 30px 24px 0 30px;
  }
  .note blockquote {
    font-family: "Handlee", cursive;
    font-size: 20px;
    line-height: 25px;
    color: var(--ink);
  }
  .note cite {
    display: block;
    margin-top: 4px;
    font-style: italic;
    font-weight: 700;
    font-size: 16px;
    line-height: 20px;
    color: var(--ink);
  }
  .pin { position: absolute; left: 130px; top: 188px; }
  .side-back .brand {
    position: absolute; left: 70px; top: 472px;
    justify-content: flex-start;
    font-size: 16px; line-height: 17px;
    text-align: left;
  }
  .side-back .brand .mark { width: 32px; height: 32px; }
  .sponsor {
    position: absolute; right: 42px; top: 476px;
    text-align: right;
    font-size: 11.5px;
    line-height: 16px;
    font-style: italic;
    color: var(--ink);
  }
  .sponsor strong { font-weight: 700; }
</style>
</head>
<body>

<section class="card side-front">
  <div class="inner">
    <div class="brand"><span class="mark"></span>LALH SCHOLAR BRIDGE INITIATIVE</div>
    <h1 class="title">CAMPUS<br>PATHWAY SEMINAR</h1>
    <p class="subtitle">A Classroom Course for<br>LALH Students Interested in College-Going</p>
    <div class="feature">
      <div class="photo" role="img" aria-label="Photo of an open course binder with a pen on a desk"></div>
      <dl class="schedule">
        <dt>Daytime Schedule:</dt>
        <dd>Wednesdays,<br>12:20 pm – 3:00 pm</dd>
        <dt>Evening Schedule:</dt>
        <dd>Wednesdays,<br>5:00 pm – 6:15 pm</dd>
      </dl>
    </div>
    <p class="enroll"><strong>To learn more and enroll</strong>:<br>visit the Scholar Bridge Initiative in Room 1412 on your registration day.<br><strong>Apply now to guarantee a space!</strong></p>
  </div>
</section>

<section class="card side-back">
  <div class="band"></div>
  <div class="frame"></div>
  <h2 class="headline">College Bound</h2>
  <div class="note">
    <blockquote>“Before taking the Campus Pathway Seminar, I wasn’t sure how I would even start. The Workshop provided me with the information that I needed to go back to college.”</blockquote>
    <cite>CPS Participant Spring 2013, Currently Attending Ravelin Community College</cite>
  </div>
  <svg class="pin" width="60" height="64" viewBox="0 0 60 64" aria-hidden="true">
    <ellipse cx="40" cy="52" rx="14" ry="5" fill="rgba(0,0,0,0.15)"/>
    <line x1="22" y1="30" x2="36" y2="50" stroke="#9aa3ad" stroke-width="3" stroke-linecap="round"/>
    <circle cx="20" cy="18" r="14" fill="#3aa6d6"/>
    <circle cx="15" cy="13" r="5" fill="#8fd2ef"/>
  </svg>
  <div class="brand"><span class="mark"></span><span>LALH SCHOLAR BRIDGE<br>INITIATIVE</span></div>
  <p class="sponsor"><strong>The Larchfield Adult Learning Hub</strong><br>is administered by Westbrook Township Community College/PVNU.</p>
</section>

</body>
</html>
```